website design for Company MVR

Our company name MVR(the grand mural limited), need design a website. It is a website that focuses on promoting art design in the world.
We will provide the existing logo design, the new website and logo should be matched to each other. The website has to include pages "Home" "Contact" "Service" and So on at least 6-8 pages. The site is mainly for publicity and promotion. We will have an existing domain and hosting.
Updates

We prefer the original design, thanks.

Target Market(s)

large public art

Industry/Entity Type

Architecture and design, large public art and sculpture manufacturer

Coding

Coded - Design and coding required

Number of Pages Required

5+ page

Requirements
Must have
• 1. the overall color has to match our logo color 2. Do not need to do any change on our logo including the color 3. Here is a similar style of the home page we like, it can be similar but must not same. Pls check the below link. https://www.velmardo.it/en-us/

```html
<!DOCTYPE html>
<html lang="en">
<head>
<meta charset="utf-8">
<title>MVR — The Grand Mural</title>
<link href="https://fonts.googleapis.com/css2?family=Lora:wght@400;600;700&family=Poppins:wght@300;400;500;700;800&display=swap" rel="stylesheet">
<style>
:root{
  --ink:#1c1c1c;
  --dark:#3b3b3b;
  --muted:#7a7a7a;
  --line:#d9d9d4;
  --paper:#ffffff;
  --cream:#f6f6f1;
  --footer:#1f1f1f;
  --star:#f2b01e;
  --panel:#ededeb;
  --sans:'Poppins',sans-serif;
  --serif:'Lora',serif;
}
*{box-sizing:border-box;margin:0;padding:0}
html,body{width:1200px;height:5128px;overflow:hidden}
body{position:relative;background:var(--paper);color:var(--ink);font-family:var(--sans)}
.abs{position:absolute}
a{color:inherit;text-decoration:none}

/* header */
.brand{left:60px;top:24px;display:flex;align-items:center;gap:12px}
.brand-mark{font-family:var(--sans);font-weight:800;font-size:34px;letter-spacing:1px;color:var(--dark)}
.brand-name{font-family:var(--sans);font-weight:400;font-size:15px;line-height:16px;letter-spacing:2px;color:var(--dark)}
.nav{left:448px;top:40px;display:flex;gap:22px;font-size:12px;color:var(--dark)}
.nav .active{border-bottom:2px solid var(--dark);padding-bottom:4px}
.header-tools{left:1015px;top:36px;display:flex;align-items:center;gap:10px;font-size:11px}

/* hero */
.hero{left:0;top:0;width:1200px;height:712px;background:var(--cream);z-index:-1}
.hero-kicker{left:708px;top:232px;font-size:17px;color:var(--dark)}
.hero-title{left:708px;top:262px;font-size:72px;line-height:76px;font-weight:700;color:var(--ink)}
.btn{display:flex;align-items:center;gap:8px}
.btn-square{width:36px;height:36px;background:var(--dark)}
.btn-label{background:var(--dark);color:#fff;font-family:var(--serif);font-size:14px;padding:10px 22px;letter-spacing:.5px}
.hero-arrows{left:1030px;top:664px;display:flex;align-items:center;gap:10px}

/* section headings */
.h2{width:1200px;left:0;text-align:center;font-family:var(--serif);font-weight:700;font-size:31px}
.sub{width:1200px;left:0;text-align:center;font-family:var(--serif);font-size:14px;color:var(--muted)}

/* exhibitions */
.exh-card{width:238px;text-align:center}
.art{display:block}
.exh-title{font-family:var(--serif);font-weight:700;font-size:14px;line-height:24px;margin-top:28px}
.exh-date{font-size:12px;color:var(--muted);margin-top:14px}

/* about */
.about-copy{left:108px;top:1494px;width:370px;font-size:10.5px;line-height:19px;color:var(--muted)}
.about-copy p+p{margin-top:18px}
.tag{width:132px;height:44px;background:#ececea;display:flex;align-items:center;justify-content:center;font-size:14px;font-weight:500;color:var(--ink)}

/* events */
.events-bg{left:0;top:1875px;width:1200px;height:1185px;background:var(--cream);z-index:-1}
.event-text{width:370px}
.event-date{font-family:var(--serif);font-size:12px;font-weight:600;display:flex;align-items:center;gap:14px}
.event-date::after{content:"";width:120px;height:1px;background:var(--line)}
.event-title{font-family:var(--serif);font-size:18px;line-height:27px;margin-top:20px}
.event-desc{font-size:10.5px;line-height:19px;color:var(--muted);margin-top:14px}

/* artists */
.artist{width:225px}
.artist-name{font-family:var(--serif);font-weight:700;font-size:17px;margin-top:16px}
.artist-site{font-size:11px;color:var(--muted)}

/* advice */
.advice-title{left:148px;top:3650px;font-family:var(--serif);font-weight:700;font-size:32px;line-height:39px}
.advice-copy{left:152px;top:3786px;font-size:11px;line-height:22px;color:var(--muted)}
.advice-link{left:214px;top:3926px;font-size:11px;color:var(--muted)}
.advice-link a{color:var(--ink);text-decoration:underline}

/* gallery */
.painting-label{left:608px;top:4320px;width:278px;text-align:center;color:#fff;font-family:var(--serif);font-size:21px}
.painting-label small{display:block;font-family:var(--sans);font-size:10px;margin-top:4px}

/* testimonials */
.stars{left:134px;top:4620px;color:var(--star);font-size:17px;letter-spacing:2px}
.testi-title{left:134px;top:4648px;font-family:var(--serif);font-weight:700;font-size:30px}
.testi-sub{left:134px;top:4696px;font-size:11px;color:var(--muted)}
.testi-quote{left:695px;top:4622px;width:385px;font-size:11px;line-height:22px;color:var(--muted)}
.testi-client{left:695px;top:4712px;font-family:var(--serif);font-weight:700;font-size:14px;display:flex;align-items:center;gap:10px}
.testi-client::before{content:"";width:22px;height:2px;background:var(--ink)}

/* footer */
.footer{left:0;top:4830px;width:1200px;height:298px;background:var(--footer);color:#fff}
.f-brand{left:60px;top:46px}
.f-brand .brand-mark,.f-brand .brand-name{color:#d8d8d8}
.f-note{left:60px;top:106px;font-size:12px;line-height:20px;color:#cfcfcf}
.f-input{left:60px;top:162px;width:300px;border-bottom:1px solid #8a8a8a;padding-bottom:8px;font-size:10px;color:#cfcfcf;display:flex;justify-content:space-between}
.f-col h4{font-family:var(--serif);font-size:13px;font-weight:600;letter-spacing:1px;color:#bdbdbd;margin-bottom:22px}
.f-col li{list-style:none;font-size:10.5px;line-height:21px;color:#d9d9d9;padding-left:18px;position:relative}
.f-col li::before{content:"";position:absolute;left:0;top:9px;width:3px;height:3px;border-radius:50%;background:#888}
.contact-row{display:flex;align-items:center;gap:14px;font-size:12px;color:#e4e4e4;margin-bottom:16px}
.socials{display:flex;gap:8px}
.social{width:36px;height:36px;background:#3a3a3a;border:1px solid #555}
.copyright{left:0;top:272px;width:1200px;text-align:center;font-size:10px;color:#bdbdbd}
</style>
</head>
<body>

<!-- HEADER -->
<header>
  <div class="abs brand"><span class="brand-mark">MVR</span><span class="brand-name">THE<br>GRAND MURAL</span></div>
  <nav class="abs nav">
    <a class="active">Home</a><a>About Us</a><a>Services</a><a>Artworks</a><a>Artists</a><a>Events</a><a>Contact Us</a>
  </nav>
  <div class="abs header-tools">
    <svg width="18" height="18" viewBox="0 0 18 18"><circle cx="7.5" cy="7.5" r="6" fill="none" stroke="#1c1c1c" stroke-width="2"/><line x1="12" y1="12" x2="17" y2="17" stroke="#1c1c1c" stroke-width="2"/></svg>
    <svg width="14" height="16" viewBox="0 0 14 16"><circle cx="7" cy="5" r="3.5" fill="none" stroke="#1c1c1c" stroke-width="1.5"/><path d="M1 15c0-4 3-6 6-6s6 2 6 6" fill="none" stroke="#1c1c1c" stroke-width="1.5"/></svg>
    <span>Sign In</span>
    <svg width="16" height="18" viewBox="0 0 16 18"><rect x="1.5" y="5" width="13" height="12" fill="none" stroke="#1c1c1c" stroke-width="1.5"/><path d="M5 5V3.5a3 3 0 0 1 6 0V5" fill="none" stroke="#1c1c1c" stroke-width="1.5"/></svg>
  </div>
</header>

<!-- HERO -->
<section>
  <div class="abs hero"></div>
  <div class="abs art" role="img" aria-label="Large colourful oil painting of an autumn forest" style="left:78px;top:150px;width:630px;height:530px;background:linear-gradient(135deg,#b8281e,#d9a12b 45%,#3d5f8a 75%,#2a2a2a)"></div>
  <p class="abs hero-kicker">Celebrating The Independence of The Artist</p>
  <h1 class="abs hero-title">Unique<br>Public Art</h1>
  <a class="abs btn" style="left:710px;top:442px">
    <span class="btn-square"></span>
    <span class="btn-label">SHOP NOW</span>
  </a>
  <div class="abs hero-arrows">
    <svg width="70" height="2"><line x1="0" y1="1" x2="70" y2="1" stroke="#555" stroke-width="1"/></svg>
    <svg width="14" height="24" viewBox="0 0 14 24"><path d="M12 2 L2 12 L12 22" fill="none" stroke="#1c1c1c" stroke-width="2"/></svg>
    <svg width="14" height="24" viewBox="0 0 14 24"><path d="M2 2 L12 12 L2 22" fill="none" stroke="#1c1c1c" stroke-width="2"/></svg>
  </div>
</section>

<!-- EXHIBITIONS -->
<section>
  <div class="abs" style="left:600px;top:735px;width:1px;height:85px;background:var(--line)"></div>
  <h2 class="abs h2" style="top:832px">Exhibitions</h2>
  <div class="abs exh-card" style="left:94px;top:904px">
    <div class="art" role="img" aria-label="Painting of a tree-lined village path" style="height:194px;background:linear-gradient(135deg,#6d7a55,#b7a98a,#3f4a36)"></div>
    <p class="exh-title">Lorem ipsum is that simple<br>text the Print Type !</p><p class="exh-date">03/04 Jan 2022</p>
  </div>
  <div class="abs exh-card" style="left:351px;top:904px">
    <div class="art" role="img" aria-label="Painting of a dancer in a red dress" style="height:194px;background:linear-gradient(135deg,#2b4fa5,#c8242a,#e89a3a)"></div>
    <p class="exh-title">Lorem ipsum is that simple<br>text the Print Type !</p><p class="exh-date">03/04 Jan 2022</p>
  </div>
  <div class="abs exh-card" style="left:609px;top:904px">
    <div class="art" role="img" aria-label="Classical painting of a gathering of figures" style="height:194px;background:linear-gradient(135deg,#3a2b22,#a56a3e,#6b2e22)"></div>
    <p class="exh-title">Lorem ipsum is that simple<br>text the Print Type !</p><p class="exh-date">03/04 Jan 2022</p>
  </div>
  <div class="abs exh-card" style="left:868px;top:904px">
    <div class="art" role="img" aria-label="Colourful painting of a reclining figure with a bird" style="height:194px;background:linear-gradient(135deg,#1f4f8f,#d6b33c,#2c7a6a)"></div>
    <p class="exh-title">Lorem ipsum is that simple<br>text the Print Type !</p><p class="exh-date">03/04 Jan 2022</p>
  </div>
  <div class="abs" style="left:250px;top:1274px;width:700px;height:1px;background:#ececea"></div>
</section>

<!-- ABOUT -->
<section>
  <h2 class="abs h2" style="top:1344px">About The Grand Mural</h2>
  <p class="abs sub" style="top:1390px">Discover The World Through Original Arts</p>
  <div class="abs about-copy">
    <p>Lorem Ipsum has been the industry's standard dummy text ever since the 1500s, when an unknown printer took a galley of type and industry scrambled it to make a type specimen book.</p>
    <p>Lorem Ipsum has been the industry's standard dummy text ever since the 1500s, when an unknown printer took a galley of type and that is scrambled it to make a type specimen book. It has survived not only five centuries, but also the leap.</p>
  </div>
  <div class="abs tag" style="left:108px;top:1675px">OIL PAINT</div>
  <div class="abs tag" style="left:250px;top:1675px">BRUSH</div>
  <div class="abs tag" style="left:108px;top:1732px">SKETCH</div>
  <div class="abs tag" style="left:250px;top:1732px">DRWING</div>
  <div class="abs art" role="img" aria-label="Artist painting at an easel in a studio full of canvases" style="left:548px;top:1463px;width:544px;height:337px;background:linear-gradient(120deg,#4a3b2e,#b08a4a,#5b6d8c,#2e2a26)"></div>
</section>

<!-- EVENTS -->
<section>
  <div class="abs events-bg"></div>
  <h2 class="abs h2" style="top:1945px">Public Art Events</h2>
  <p class="abs sub" style="top:1992px">Our Latest Collection Of Public Art</p>

  <div class="abs art" role="img" aria-label="Abstract painting of stylised figures in bold colours" style="left:148px;top:2060px;width:424px;height:240px;background:linear-gradient(135deg,#1d3f8a,#e8e1cf,#e9b52a,#c9302c)"></div>
  <div class="abs event-text" style="left:634px;top:2096px">
    <p class="event-date">05 January 2022</p>
    <p class="event-title">Lorem Ipsum has been the industry's<br>standard dummy text ever</p>
    <p class="event-desc">Lorem Ipsum has been the industry's standard dummy text ever since the 1500s, when an unknown printer.</p>
  </div>

  <div class="abs event-text" style="left:176px;top:2412px">
    <p class="event-date">05 January 2022</p>
    <p class="event-title">Lorem Ipsum has been the industry's<br>standard dummy text ever</p>
    <p class="event-desc">Lorem Ipsum has been the industry's standard dummy text ever since the 1500s, when an unknown printer.</p>
  </div>
  <div class="abs art" role="img" aria-label="Painting of a violinist beside a sculpture" style="left:632px;top:2360px;width:424px;height:240px;background:linear-gradient(135deg,#3a6f8f,#d8a85a,#6e3b2a,#e7dcc4)"></div>

  <div class="abs art" role="img" aria-label="Painting of a saxophone player" style="left:148px;top:2660px;width:424px;height:240px;background:linear-gradient(135deg,#5a4a3c,#b9a58c,#3b3230)"></div>
  <div class="abs event-text" style="left:634px;top:2696px">
    <p class="event-date">05 January 2022</p>
    <p class="event-title">Lorem Ipsum has been the industry's<br>standard dummy text ever</p>
    <p class="event-desc">Lorem Ipsum has been the industry's standard dummy text ever since the 1500s, when an unknown printer.</p>
  </div>

  <a class="abs btn" style="left:494px;top:2946px">
    <span class="btn-square"></span>
    <span class="btn-label">VIEW ALL EVNTS</span>
  </a>
</section>

<!-- ARTISTS -->
<section>
  <h2 class="abs h2" style="top:3130px">The Artists Collectors Love Right Now</h2>
  <svg class="abs" style="left:180px;top:3320px" width="14" height="30" viewBox="0 0 14 30"><path d="M12 2 L2 15 L12 28" fill="none" stroke="#888" stroke-width="1.5"/></svg>
  <svg class="abs" style="left:1004px;top:3320px" width="14" height="30" viewBox="0 0 14 30"><path d="M2 2 L12 15 L2 28" fill="none" stroke="#888" stroke-width="1.5"/></svg>
  <div class="abs artist" style="left:240px;top:3207px">
    <div class="art" role="img" aria-label="Portrait photo of a featured artist" style="height:211px;background:linear-gradient(135deg,#c9b7a4,#6b5a4c,#d8d2ca)"></div>
    <p class="artist-name">Artist Name</p><p class="artist-site">something.com</p>
  </div>
  <div class="abs artist" style="left:488px;top:3207px">
    <div class="art" role="img" aria-label="Portrait photo of a featured artist" style="height:211px;background:linear-gradient(135deg,#4a4c50,#2d2f33,#6a6d72)"></div>
    <p class="artist-name">Artist Name</p><p class="artist-site">something.com</p>
    <div style="margin-top:20px;height:1px;background:var(--line)"></div>
  </div>
  <div class="abs artist" style="left:735px;top:3207px">
    <div class="art" role="img" aria-label="Portrait photo of a featured artist" style="height:211px;background:linear-gradient(135deg,#b98e62,#5c3e28,#e0d6c8)"></div>
    <p class="artist-name">Artist Name</p><p class="artist-site">something.com</p>
  </div>
</section>

<!-- ADVICE -->
<section>
  <div class="abs" aria-hidden="true" style="left:600px;top:3572px;width:535px;height:458px;background:var(--panel)"></div>
  <div class="abs art" role="img" aria-label="Photo of a smiling painter in an apron holding a palette and brush" style="left:610px;top:3590px;width:440px;height:440px;background:linear-gradient(160deg,#cfd3cf,#8fb3b0 40%,#3a3a3a 75%,#e6d2b0)"></div>
  <h2 class="abs advice-title">Get Free Personalized<br>Advice From our Expert<br>art Advisors, 24/7</h2>
  <p class="abs advice-copy">Looking For Advice?<br>A Specially Commissioned Piece?<br>Discover our Online art Gallery with Free Art Advisory!</p>
  <a class="abs btn" style="left:148px;top:3876px">
    <span class="btn-square"></span>
    <span class="btn-label">SPEAK WITH US DIRECTLY</span>
  </a>
  <p class="abs advice-link">Or &nbsp;<a>Contact Us VIA E-mail</a></p>
</section>

<!-- GALLERY -->
<section>
  <h2 class="abs h2" style="top:4092px">Buy Original Art Online On Our Art Gallery.</h2>
  <div class="abs art" role="img" aria-label="Etching-style artwork of a sailing ship on waves" style="left:22px;top:4180px;width:278px;height:335px;background:linear-gradient(135deg,#2a2a2a,#8a7a60,#3a3530)"></div>
  <div class="abs art" role="img" aria-label="Painting of a woman in a flowing yellow dress" style="left:316px;top:4180px;width:278px;height:335px;background:linear-gradient(135deg,#5a2a6a,#e0b25a,#c06b8a)"></div>
  <div class="abs art" role="img" aria-label="Abstract cubist portrait painting" style="left:608px;top:4180px;width:278px;height:335px;background:linear-gradient(135deg,#1e2a5a,#c84a3a,#e8c23a);border:8px solid #2a2a2a"></div>
  <div class="abs" style="left:608px;top:4180px;width:278px;height:335px;background:rgba(30,30,30,.55)"></div>
  <p class="abs painting-label">Painting Name<small>Artist Name</small></p>
  <div class="abs art" role="img" aria-label="Painting of woodpeckers on a tree trunk" style="left:900px;top:4180px;width:278px;height:335px;background:linear-gradient(135deg,#dcd8cc,#6b4a30,#b02a22,#e8e4da)"></div>
</section>

<!-- TESTIMONIALS -->
<section>
  <p class="abs stars">★★★★★</p>
  <h2 class="abs testi-title">Testimonials</h2>
  <p class="abs testi-sub">What our client say About Us</p>
  <div class="abs" style="left:134px;top:4732px;display:flex;gap:8px">
    <svg width="10" height="18" viewBox="0 0 10 18"><path d="M8 2 L2 9 L8 16" fill="none" stroke="#555" stroke-width="1.5"/></svg>
    <svg width="10" height="18" viewBox="0 0 10 18"><path d="M2 2 L8 9 L2 16" fill="none" stroke="#555" stroke-width="1.5"/></svg>
  </div>
  <div class="abs art" role="img" aria-label="Expressive painting of a figure in gold and dark tones" style="left:430px;top:4595px;width:213px;height:165px;background:linear-gradient(135deg,#2a2030,#c9962a,#5a2a3a);border:3px solid #1c1c1c"></div>
  <p class="abs testi-quote">Lorem Ipsum has been the industry's standard dummy text ever since the, when an unknown printer took a galley of type and scrambled it to make a type specimen book.</p>
  <p class="abs testi-client">Client Name</p>
</section>

<!-- FOOTER -->
<footer class="abs footer">
  <div class="abs brand f-brand"><span class="brand-mark">MVR</span><span class="brand-name">THE<br>GRAND MURAL</span></div>
  <p class="abs f-note">Would you like to receive our exclusive<br>update for signup !</p>
  <div class="abs f-input"><span>Enter Email</span>
    <svg width="18" height="16" viewBox="0 0 18 16"><path d="M1 7 L17 1 L12 15 L9 9 Z" fill="#e4e4e4"/></svg>
  </div>
  <div class="abs f-col" style="left:392px;top:52px">
    <h4>SITEMAP</h4>
    <ul><li>Home</li><li>About Us</li><li>Services</li><li>Artworks</li><li>Artiste Events</li><li>Contact Us</li></ul>
  </div>
  <div class="abs f-col" style="left:646px;top:52px">
    <h4>CUSTOMER SERVICES</h4>
    <ul><li>Legal Notices</li><li>General Terms &amp; Conditions</li><li>Customer testimonials</li><li>Offer a Gift Card</li><li>Free art advisory</li><li>Commission an Artist</li></ul>
  </div>
  <div class="abs f-col" style="left:900px;top:52px">
    <h4>CONTACT US</h4>
    <p class="contact-row"><svg width="16" height="12" viewBox="0 0 16 12"><rect width="16" height="12" fill="#e4e4e4"/><path d="M0 0 L8 7 L16 0" fill="none" stroke="#1f1f1f" stroke-width="1.5"/></svg>info@thegrandmural.com</p>
    <p class="contact-row" style="font-size:14px"><svg width="16" height="16" viewBox="0 0 16 16"><path d="M3 1 L6 1 L7 5 L5 6.5 C6 9 7 10 9.5 11 L11 9 L15 10 L15 13 C15 14 14 15 13 15 C6 15 1 10 1 3 C1 2 2 1 3 1 Z" fill="#e4e4e4"/></svg>123 456 7890</p>
    <div class="socials">
      <span class="social" aria-label="Social profile"></span>
      <span class="social" aria-label="Social profile"></span>
      <span class="social" aria-label="Social profile"></span>
    </div>
  </div>
  <p class="abs copyright">©THE GRAND MURAL – 2021 All rights reserved.</p>
</footer>

</body>
</html>
```